Re-Brand of TindelMox along with a new website design

TindelMox Ltd are a software & database development company using technologies such as PHP, C#, HTML, JQuery, Flex, AS3, MySQL, Oracle, MSSQL. We like to target all types of business from small to large.

We are great at coding but rubbish at design so thats where we need your help!

We want a complete re-brand of TindelMox including logo, website design, and business cards.

We would like a design that is clean but other than that, please feel free to be creative.

****Logo****
We are looking for a logo that appears professional but with a splash of colour that indicates a creative side. Please see below some logos that we like the look of:

We like this one because it has a nice simple and clear font for the name of the company but also an icon which is colourful and stands out. http://markvault.example/2013/03/brivelo/

We like this one because it is very clean, simple and again very clear. http://markvault.example/2013/03/quantorels/

http://markvault.example/2013/03/tide-lamp/
http://markvault.example/2013/02/velmorin/
http://markvault.example/2013/01/art-gallery-tarnwick/

As you will see from all of these examples, the font is very clear but there is always a graphic representing the company too. This is what we like.

****Website****
These are some of the examples of websites we like:
https://www.zestrune.example/
https://www.chatterlane.example/home
http://www.haldenimagery.example/
http://www.vistor.example/
http://quillbay.example/
https://www.usebriefnest.example/personal-intros
http://www.marmotpanel.example/

The current site can be found at tindelmox.example.uk

Reason: We have extended the deadline of the project by 5 days as I realise the original deadline was very tight.

Software

Requirements
Must have
• Website must have the following pages
Home
Services
Projects
About Us
Contact Us

```html
<!DOCTYPE html>
<html lang="en">
<head>
<meta charset="utf-8">
<title>TindelMox Business Cards</title>
<link href="https://fonts.googleapis.com/css2?family=Montserrat:wght@300;400;700;800&display=swap" rel="stylesheet">
<style>
  :root {
    --ink-dark: #4a4a4c;
    --ink-light: #8a8a8c;
    --brand-green: #7cc142;
    --card-edge: #b9b9bb;
    --paper: #ffffff;
  }
  * { margin: 0; padding: 0; box-sizing: border-box; }
  html, body {
    width: 1200px;
    height: 1183px;
    overflow: hidden;
    background: var(--paper);
    font-family: "Montserrat", Arial, sans-serif;
  }
  .canvas {
    position: relative;
    width: 1200px;
    height: 1183px;
  }
  .card {
    position: absolute;
    left: 220px;
    width: 703px;
    height: 404px;
    border: 2px solid var(--card-edge);
    background: var(--paper);
    overflow: hidden;
  }
  .card--front { top: 148px; }
  .card--back  { top: 586px; }

  .wordmark {
    position: absolute;
    inset: 0;
    display: flex;
    align-items: center;
    justify-content: center;
    gap: 14px;
  }
  .wordmark__name {
    font-weight: 800;
    font-size: 60px;
    letter-spacing: 1px;
    color: var(--ink-dark);
  }
  .wordmark__dot {
    width: 16px;
    height: 16px;
    border-radius: 50%;
    background: var(--brand-green);
  }

  .holder-name {
    position: absolute;
    top: 136px;
    left: 0;
    width: 100%;
    text-align: center;
    font-weight: 700;
    font-size: 33px;
    letter-spacing: 1px;
    color: var(--brand-green);
  }
  .corner-dot {
    position: absolute;
    left: -12px;
    top: 304px;
    width: 44px;
    height: 44px;
    border-radius: 50%;
    background: var(--brand-green);
  }
  .contact {
    position: absolute;
    right: 16px;
    bottom: 14px;
    list-style: none;
    text-align: right;
    font-weight: 300;
    font-size: 22px;
    line-height: 31px;
    color: var(--ink-light);
  }
  .contact__web { color: var(--brand-green); }
</style>
</head>
<body>
  <main class="canvas">
    <section class="card card--front" aria-label="Card front">
      <div class="wordmark">
        <span class="wordmark__name">TINDELMOX</span>
        <span class="wordmark__dot"></span>
      </div>
    </section>

    <section class="card card--back" aria-label="Card back">
      <h1 class="holder-name">ROWAN HADLEY</h1>
      <span class="corner-dot"></span>
      <ul class="contact">
        <li>email: rowan@tindelmox.example.uk</li>
        <li>tel: 01632 960600</li>
        <li>mob: 07700 900411</li>
        <li class="contact__web">tindelmox.example.uk</li>
      </ul>
    </section>
  </main>
</body>
</html>
```